Osteopath Advert Flyer for 20% discount

Osteopathic treatment services (much like the flyer design I found on google which brought me to your website - "Bodywise Restful Healing"
I very much like the left side of that screenshot with the graphic design body rather than a real person.
If double sided, here are further details for what it is I do (this is optional if it is double sided). Ideally one side eye catching and the other with more information.
____________________________
Osteopathy can offer great results for those seeking immediate care with painful conditions and also for those wishing to invest in long-term health solutions. Treatments are tailored to the individual’s need, regardless of age or condition, my goal is to provide the best medical care whether it be treatment or more appropriate referral.

Osteopathy focuses on health promotion and disease prevention in order to help each person achieve a high level of wellness.

Osteopathy uses conventional medical assessment and techniques when gathering detail during diagnostic procedures. However, the real strength of osteopathy lies within the unique approach to which a patient and the condition are assessed and treated. Each patient is assessed from both a mechanical and functional viewpoint and treatment is based on these findings and patient requirements. Manual treatment methods are applied to suit the needs of the individual patient.

The overall goal is to achieve wellness by restoring balance and flexibility to the whole body.
_____________________________
I live in a small Island called Jersey and word-of-mouth is everything here. Therefore, I'd like a flyer that clearly indicates I treat people and aim to help people out of pain and injury but also give a very relaxing and enjoyable experience. So, not too clinical but also not to imaginary/idealistic massage room spa treatment.

Osteopathy is more or less in between a physio and a chiropractor (with regards to design style of this flyer). Of course it is somewhat very different to those professions, however, for this purpose the overall aim/style would be similar.

Please note: I do not particularly desire being on the flyer myself, however, it could be quite useful so I am happy for you to decide whether it may be of benefit.The aim is to attract the eye of the people walking past the flyer and to look professional but also interesting as many people will not have seen an osteopath before.

Thank you!

Target Market(s)

All humans above ages for 10

Industry/Entity Type

Healthcare

Font styles to use
Serif
Sans Serif

Colors
3377b5
33a6d7
ffffff
34a7d7
3277b5
85acd3
85cae6

Requirements
Must have
• 07461 352 417
contact@belvantoske.co.uk
www.belvantoske.co.uk

Copper Mead Clinic
La Rue Des Pins
St Lawrence
Jersey
JE2 4QW

20% off with this flyer (*for initial consultation only*)
Nice to have
• Initial Consultation £55 for 45 minutes
Follow-Up Treatment £50 for 30 minutes

Treatment areas (much like in the flyers I attached as screenshots from google)
Headaches
Neck pain
Shoulder pain
Elbow and hand pain
Back pain
Hip pain
Knee pain
Ankle and foot pain
Arthritic pains
Chronic pain
Should not have
• No age range/indication of ages applicable as I wish to help and treat everyone (above the age of 10 for I do not specialise in paediatric osteopathy)

```html
<!DOCTYPE html>
<html lang="en">
<head>
<meta charset="utf-8">
<title>Bodywise Restful Healing – Osteopathy Flyers</title>
<link rel="stylesheet" href="https://fonts.googleapis.com/css2?family=Oswald:wght@500;600&family=Open+Sans:wght@400;600;700&display=swap">
<style>
:root{
  --navy:#233e8b;
  --deep:#1c2f6e;
  --blue:#3277b5;
  --sky:#33a6d7;
  --pale:#85cae6;
  --mist:#85acd3;
  --ink:#3a3a3a;
  --white:#ffffff;
  --stage:#e9ecef;
}
*{box-sizing:border-box;margin:0;padding:0}
html,body{width:1200px;height:847px;overflow:hidden;background:var(--stage)}
body{position:relative;font-family:"Open Sans",Arial,sans-serif;color:var(--ink)}
.icon-defs{position:absolute;width:0;height:0}
.flyer{position:absolute;top:66px;width:475px;height:672px;background:var(--white);overflow:hidden;box-shadow:0 3px 10px rgba(0,0,0,.18)}
.flyer--benefits{left:90px}
.flyer--treatments{left:620px}
.flyer__art{position:absolute;inset:0;width:475px;height:672px}
.brand{position:absolute;left:18px;top:20px;display:flex;align-items:center;gap:8px}
.brand__dot{width:12px;height:12px;border-radius:50%;background:var(--blue)}
.brand__name{font-weight:600;font-size:15px;color:var(--blue)}
.headline{position:absolute;left:14px;top:286px;font-family:"Oswald",Arial,sans-serif;font-weight:500;font-size:19px;line-height:23px;color:var(--navy);text-transform:uppercase;letter-spacing:.2px}
.intro{position:absolute;left:14px;top:311px;width:315px;font-size:8.2px;line-height:11.2px;text-align:justify}
.callout{position:absolute;left:12px;top:385px;width:320px;height:40px;border-radius:8px;background:linear-gradient(var(--blue),var(--navy));border:2px solid var(--mist);color:var(--white);font-weight:700;font-size:8.2px;line-height:1.35;display:flex;align-items:center;justify-content:center;text-align:center;padding:0 10px;box-shadow:0 2px 5px rgba(0,0,0,.3)}
.subhead{position:absolute;left:14px;top:438px;font-family:"Oswald",Arial,sans-serif;font-weight:500;font-size:12.5px;line-height:18px;color:var(--navy)}
.benefits{position:absolute;left:14px;top:459px;width:318px;display:grid;grid-template-columns:1fr 1fr;gap:6px 10px;list-style:none}
.benefit{display:flex;gap:4px}
.benefit h3{font-size:8.4px;line-height:11px;font-weight:600;color:var(--blue)}
.benefit p{font-size:7px;line-height:8.8px}
.bullet{flex:none;width:9px;height:9px;margin-top:1px}
.contact{position:absolute;left:14px;top:582px;color:var(--white)}
.contact__title{font-family:"Oswald",Arial,sans-serif;font-weight:500;font-size:18px;line-height:24px;margin-bottom:2px}
.contact__list{list-style:none;font-size:8.6px;line-height:14.5px}
.contact__list li{display:flex;align-items:center;gap:6px}
.contact__list svg{width:8px;height:8px;flex:none}
.tab{position:absolute;left:0;top:318px;width:275px;height:25px;background:var(--navy);clip-path:polygon(0 0,96% 0,100% 100%,0 100%);color:var(--white);font-family:"Oswald",Arial,sans-serif;font-weight:500;font-size:15px;line-height:25px;padding-left:18px}
.treatments{position:absolute;left:24px;top:351px;width:320px;display:grid;grid-template-columns:176px 1fr;grid-auto-flow:column;grid-template-rows:repeat(5,25px);list-style:none}
.treatments li{display:flex;align-items:center;gap:8px;font-family:"Oswald",Arial,sans-serif;font-weight:500;font-size:12px;color:var(--blue);text-transform:uppercase}
.treatments .bullet{width:10px;height:10px;margin:0}
.price{position:absolute;top:486px;height:62px;border-radius:9px;background:linear-gradient(var(--blue),var(--navy));border:3px solid #d7dfec;box-shadow:0 3px 6px rgba(0,0,0,.35);color:var(--white);display:flex;align-items:center;gap:6px;padding-left:10px}
.price--initial{left:22px;width:158px}
.price--follow{left:198px;width:160px}
.price__amount{font-family:"Oswald",Arial,sans-serif;font-weight:600;font-size:33px;line-height:1}
.price__label{font-family:"Oswald",Arial,sans-serif;font-weight:500;font-size:10.5px;line-height:1.05;text-transform:uppercase}
.price__label small{display:block;font-family:"Open Sans",Arial,sans-serif;font-weight:400;font-size:7.5px;text-transform:none}
.offer{position:absolute;left:363px;top:16px;width:150px;height:44px;transform:rotate(45deg);text-align:center;color:var(--white);font-family:"Oswald",Arial,sans-serif;font-weight:500;line-height:1.1}
.offer__big{display:block;font-size:12px}
.offer__line{display:block;font-size:10.5px}
.offer small{display:block;font-family:"Open Sans",Arial,sans-serif;font-style:italic;font-size:6.3px;line-height:1.2}
.practitioner{position:absolute;left:337px;top:350px;width:116px;height:26px;border-radius:8px;background:var(--blue);color:var(--white);font-family:"Oswald",Arial,sans-serif;font-weight:500;font-size:8px;line-height:1.2;text-align:center;padding-top:2px}
</style>
</head>
<body>

<svg class="icon-defs" aria-hidden="true">
  <symbol id="arrow-bullet" viewBox="0 0 10 10"><circle cx="5" cy="5" r="5" fill="#3277b5"/><path d="M4 2.5 6.5 5 4 7.5" fill="none" stroke="#fff" stroke-width="1.4"/></symbol>
  <symbol id="icon-phone" viewBox="0 0 10 10"><path d="M2 1 4 3 3 4.5C4 6 5 7 5.5 7L7 6 9 8 7.5 9.5C4 9 1 6 .5 2.5Z" fill="#fff"/></symbol>
  <symbol id="icon-mail" viewBox="0 0 10 10"><rect x=".5" y="2" width="9" height="6" fill="none" stroke="#fff"/><path d="M.5 2 5 5.5 9.5 2" fill="none" stroke="#fff"/></symbol>
  <symbol id="icon-web" viewBox="0 0 10 10"><circle cx="5" cy="5" r="4.2" fill="none" stroke="#fff"/><path d="M1 5H9M5 1C3 3.5 3 6.5 5 9M5 1C7 3.5 7 6.5 5 9" fill="none" stroke="#fff" stroke-width=".8"/></symbol>
  <symbol id="icon-pin" viewBox="0 0 10 10"><path d="M5 .5C2.8.5 1.5 2 1.5 4 1.5 6.5 5 9.5 5 9.5S8.5 6.5 8.5 4C8.5 2 7.2.5 5 .5Z" fill="#fff"/><circle cx="5" cy="4" r="1.3" fill="#233e8b"/></symbol>
</svg>

<!-- Side one: benefits -->
<article class="flyer flyer--benefits">
  <svg class="flyer__art" viewBox="0 0 475 672">
    <defs>
      <clipPath id="benefitsPhotoClip"><path d="M0 104 C70 70 150 30 226 0 H475 V268 C420 262 360 282 300 278 C200 270 90 215 0 200 Z"/></clipPath>
      <linearGradient id="parkTones" x1="0" y1="0" x2="1" y2="1"><stop offset="0" stop-color="#6f7f5a"/><stop offset=".45" stop-color="#3d6fa8"/><stop offset="1" stop-color="#8a7a62"/></linearGradient>
      <radialGradient id="anatomyTones"><stop offset="0" stop-color="#3f7fd1"/><stop offset="1" stop-color="#0c1f55"/></radialGradient>
      <linearGradient id="bandTone" x1="0" y1="0" x2="0" y2="1"><stop offset="0" stop-color="#2b4a9a"/><stop offset="1" stop-color="#1c2f6e"/></linearGradient>
    </defs>
    <g role="img" aria-label="Photo: man in a blue T-shirt holding his lower back in a park, spine glowing">
      <rect width="475" height="300" fill="url(#parkTones)" clip-path="url(#benefitsPhotoClip)"/>
    </g>
    <path d="M0 104 C70 70 150 30 226 0" fill="none" stroke="var(--blue)" stroke-width="7"/>
    <path d="M0 200 C90 215 200 270 300 278 C360 282 420 262 475 268" fill="none" stroke="var(--blue)" stroke-width="6"/>
    <path d="M0 212 C90 228 200 282 290 290" fill="none" stroke="var(--mist)" stroke-width="2"/>
    <path d="M352 300 C382 400 382 520 338 590 L356 596 C398 520 400 400 374 296 Z" fill="var(--blue)" opacity=".85"/>
    <path d="M0 566 C150 560 300 590 475 600 V672 H0 Z" fill="url(#bandTone)"/>
    <path d="M0 558 C150 552 300 582 475 592" fill="none" stroke="var(--sky)" stroke-width="3"/>
    <g role="img" aria-label="Illustration: glowing shoulder joint">
      <circle cx="405" cy="308" r="50" fill="url(#anatomyTones)" stroke="#fff" stroke-width="4"/></g>
    <g role="img" aria-label="Illustration: glowing elbow joint">
      <circle cx="405" cy="406" r="50" fill="url(#anatomyTones)" stroke="#fff" stroke-width="4"/></g>
    <g role="img" aria-label="Illustration: glowing wrist and hand bones">
      <circle cx="405" cy="504" r="50" fill="url(#anatomyTones)" stroke="#fff" stroke-width="4"/></g>
    <g role="img" aria-label="Illustration: glowing forearm and hand">
      <circle cx="405" cy="602" r="50" fill="url(#anatomyTones)" stroke="#fff" stroke-width="4"/></g>
  </svg>

  <div class="brand"><span class="brand__dot"></span><span class="brand__name">Belvan Toske</span></div>

  <h1 class="headline">Bodywise Restful Healing</h1>
  <p class="intro">Osteopathy can offer great results for those seeking immediate care with painful conditions and also for those wishing to invest in long-term health solutions. Treatments are tailored to the individual’s need, regardless of age or condition, my goal is to provide the best medical care whether it be treatment or more appropriate referral.</p>
  <p class="callout">Osteopathy focuses on health promotion and disease prevention in order to help each person achieve a high level of wellness.</p>

  <h2 class="subhead">THE BENEFITS OF OSTEOPATHY</h2>
  <ul class="benefits">
    <li class="benefit"><svg class="bullet"><use href="#arrow-bullet"/></svg>
      <div><h3>Manage Chronic Pain</h3><p>Restores musculoskeletal system, underlying tissues, including organs, as well.</p></div></li>
    <li class="benefit"><svg class="bullet"><use href="#arrow-bullet"/></svg>
      <div><h3>Promote Fluid Flow</h3><p>Increase circulation into the body, reduce blood pressure, decrease inflammation and bodily detox.</p></div></li>
    <li class="benefit"><svg class="bullet"><use href="#arrow-bullet"/></svg>
      <div><h3>Prevent Injury</h3><p>Osteopathic treatments increase muscular flexion and resilience, thereby increasing range of motion and preventing tearing.</p></div></li>
    <li class="benefit"><svg class="bullet"><use href="#arrow-bullet"/></svg>
      <div><h3>Aid Relaxation</h3><p>Increase dopamine levels, and promote relaxation and wellness. Improving circulation, lymphatic flow, and vascular response.</p></div></li>
  </ul>

  <section class="contact">
    <h2 class="contact__title">CONTACT US:</h2>
    <ul class="contact__list">
      <li><svg><use href="#icon-phone"/></svg>07461 352 417</li>
      <li><svg><use href="#icon-mail"/></svg>contact@belvantoske.co.uk</li>
      <li><svg><use href="#icon-web"/></svg>www.belvantoske.co.uk</li>
      <li><svg><use href="#icon-pin"/></svg>La Rue Des Pins St Lawrence Jersey JE2 4QW</li>
    </ul>
  </section>
</article>

<!-- Side two: treatments and prices -->
<article class="flyer flyer--treatments">
  <svg class="flyer__art" viewBox="0 0 475 672">
    <defs>
      <clipPath id="treatPhotoClip"><path d="M0 104 C70 70 150 30 226 0 H475 V268 C420 262 360 282 300 278 C200 270 90 215 0 200 Z"/></clipPath>
      <linearGradient id="golfTones" x1="0" y1="0" x2="1" y2="1"><stop offset="0" stop-color="#5f7250"/><stop offset=".4" stop-color="#2f5fa8"/><stop offset="1" stop-color="#7fa25a"/></linearGradient>
      <linearGradient id="bandTone2" x1="0" y1="0" x2="0" y2="1"><stop offset="0" stop-color="#2b4a9a"/><stop offset="1" stop-color="#1c2f6e"/></linearGradient>
      <linearGradient id="spineTones" x1="0" y1="0" x2="1" y2="1"><stop offset="0" stop-color="#33a6d7"/><stop offset="1" stop-color="#0d2a6a"/></linearGradient>
      <linearGradient id="portraitTones" x1="0" y1="0" x2="0" y2="1"><stop offset="0" stop-color="#c9d4e2"/><stop offset="1" stop-color="#e9eef5"/></linearGradient>
    </defs>
    <g role="img" aria-label="Photo: man in a blue polo shirt holding his lower back on a golf course">
      <rect width="475" height="300" fill="url(#golfTones)" clip-path="url(#treatPhotoClip)"/>
    </g>
    <path d="M0 104 C70 70 150 30 226 0" fill="none" stroke="var(--blue)" stroke-width="7"/>
    <path d="M0 200 C90 215 200 270 300 278 C360 282 420 262 475 268" fill="none" stroke="var(--blue)" stroke-width="6"/>
    <path d="M0 212 C90 228 200 282 290 290" fill="none" stroke="var(--mist)" stroke-width="2"/>
    <path d="M430 370 C455 380 468 395 475 410 V380 C465 372 450 366 430 370 Z" fill="var(--blue)"/>
    <path d="M355 0 H475 V120 Z" fill="var(--navy)"/>
    <path d="M355 0 L475 120 C430 100 380 60 355 0 Z" fill="#eef1f5" stroke="#c7ced8" stroke-width=".8"/>
    <g role="img" aria-label="Illustration: glowing lower spine and pelvis of a figure">
      <path d="M250 560 C300 520 360 540 420 540 C450 540 465 530 475 520 V672 H250 Z" fill="url(#spineTones)"/></g>
    <path d="M0 566 C120 556 220 580 320 605 C360 615 420 640 475 650 V672 H0 Z" fill="url(#bandTone2)"/>
    <path d="M0 558 C120 548 220 572 320 597" fill="none" stroke="var(--sky)" stroke-width="3"/>
    <g role="img" aria-label="Photo: the osteopath in a white clinic tunic">
      <circle cx="394" cy="310" r="72" fill="url(#portraitTones)" stroke="var(--blue)" stroke-width="5"/>
      <circle cx="394" cy="310" r="66" fill="none" stroke="#fff" stroke-width="3"/></g>
  </svg>

  <div class="brand"><span class="brand__dot"></span><span class="brand__name">Belvan Toske</span></div>
  <p class="offer"><span class="offer__big">20% OFF</span><span class="offer__line">WITH THIS FLYER</span><small>*for initial consultation only*</small></p>

  <h1 class="headline">Bodywise Restful Healing</h1>
  <h2 class="tab">OUR TREATMENTS</h2>
  <div class="practitioner">BELVAN TOSKE<br>OSTEOPATH &amp; NATUROPATH</div>

  <ul class="treatments">
    <li><svg class="bullet"><use href="#arrow-bullet"/></svg>Headaches</li>
    <li><svg class="bullet"><use href="#arrow-bullet"/></svg>Neck pain</li>
    <li><svg class="bullet"><use href="#arrow-bullet"/></svg>Shoulder pain</li>
    <li><svg class="bullet"><use href="#arrow-bullet"/></svg>Elbow and hand pain</li>
    <li><svg class="bullet"><use href="#arrow-bullet"/></svg>Back pain</li>
    <li><svg class="bullet"><use href="#arrow-bullet"/></svg>Hip pain</li>
    <li><svg class="bullet"><use href="#arrow-bullet"/></svg>Knee pain</li>
    <li><svg class="bullet"><use href="#arrow-bullet"/></svg>Ankle and foot pain</li>
    <li><svg class="bullet"><use href="#arrow-bullet"/></svg>Arthritic pains</li>
    <li><svg class="bullet"><use href="#arrow-bullet"/></svg>Chronic pain</li>
  </ul>

  <div class="price price--initial"><span class="price__amount">£55</span><span class="price__label">Initial<br>Consultation<small>for 45 minutes</small></span></div>
  <div class="price price--follow"><span class="price__amount">£50</span><span class="price__label">Follow-up<br>Treatment<small>for 30 minutes</small></span></div>

  <section class="contact">
    <h2 class="contact__title">CONTACT US:</h2>
    <ul class="contact__list">
      <li><svg><use href="#icon-phone"/></svg>07461 352 417</li>
      <li><svg><use href="#icon-mail"/></svg>contact@belvantoske.co.uk</li>
      <li><svg><use href="#icon-web"/></svg>www.belvantoske.co.uk</li>
      <li><svg><use href="#icon-pin"/></svg>La Rue Des Pins St Lawrence Jersey JE2 4QW</li>
    </ul>
  </section>
</article>

</body>
</html>
```